KVRo Business Cards

We need a business card design. We are a Technology (Audio Visual) design, sales and installation company. Looking for a double sided design, clean

Contact Information for Business Card

Clean, modern look, 2 sided

Font styles to use
Sans Serif

```html
<!DOCTYPE html>
<html lang="en">
<head>
<meta charset="utf-8">
<title>KVRo Business Cards</title>
<link href="https://fonts.googleapis.com/css2?family=Poppins:wght@400;500;700&display=swap" rel="stylesheet">
<style>
  :root {
    --navy: #1b3042;
    --navy-soft: #243a4e;
    --orange: #f7941d;
    --white: #ffffff;
    --ink: #1b3042;
    --backdrop: #2a2a2c;
  }
  * { margin: 0; padding: 0; box-sizing: border-box; }
  html, body { width: 1200px; height: 880px; overflow: hidden; }
  body {
    background: var(--backdrop);
    font-family: "Poppins", sans-serif;
    position: relative;
  }
  .card {
    position: absolute;
    width: 560px;
    height: 320px;
    border-radius: 18px;
    overflow: hidden;
  }
  /* Back side */
  .card-back {
    left: 80px; top: 90px;
    background: var(--navy);
  }
  .card-back .decor { position: absolute; inset: 0; }
  .card-back .brand {
    position: absolute;
    left: 0; right: 0; top: 118px;
    text-align: center;
    color: var(--white);
    font-weight: 700;
    font-size: 64px;
    letter-spacing: 1px;
    line-height: 1;
  }
  .card-back .site {
    position: absolute;
    left: 0; right: 0; bottom: 34px;
    text-align: center;
    color: var(--white);
    font-weight: 700;
    font-size: 15px;
    letter-spacing: 1px;
  }
  /* Front side */
  .card-front {
    left: 560px; top: 470px;
    background: var(--white);
  }
  .card-front .decor { position: absolute; inset: 0; }
  .card-front .brand {
    position: absolute;
    left: 36px; top: 46px;
    color: var(--ink);
    font-weight: 700;
    font-size: 58px;
    line-height: 1;
    letter-spacing: 1px;
  }
  .card-front .person { position: absolute; left: 40px; top: 128px; }
  .person .name {
    color: var(--ink);
    font-weight: 700;
    font-size: 21px;
    line-height: 1.1;
  }
  .person .title {
    color: var(--orange);
    font-weight: 500;
    font-size: 13px;
    margin-top: 2px;
  }
  .contacts { list-style: none; margin-top: 10px; }
  .contacts li {
    display: flex; align-items: center; gap: 8px;
    color: var(--ink);
    font-size: 13px;
    line-height: 19px;
  }
  .contacts svg { width: 11px; height: 11px; fill: var(--orange); flex: none; }
  .address {
    margin-top: 8px;
    color: var(--ink);
    font-size: 13px;
    line-height: 17px;
    font-style: normal;
  }
</style>
</head>
<body>

<section class="card card-back" aria-label="Card back">
  <svg class="decor" viewBox="0 0 560 320" preserveAspectRatio="none" aria-hidden="true">
    <polygon points="330,0 420,0 300,320 210,320" fill="var(--navy-soft)"/>
  </svg>
  <div class="brand">KVRo</div>
  <div class="site">WWW.KVRO.COM</div>
</section>

<section class="card card-front" aria-label="Card front">
  <svg class="decor" viewBox="0 0 560 320" preserveAspectRatio="none" aria-hidden="true">
    <polygon points="400,0 560,0 560,260" fill="var(--navy)"/>
    <polygon points="330,0 400,0 560,260 560,320 500,320" fill="var(--orange)"/>
    <rect x="0" y="0" width="0" height="0"/>
  </svg>
  <div class="brand">KVRo</div>
  <div class="person">
    <div class="name">ALEX MORROW</div>
    <div class="title">CEO/FOUNDER</div>
    <ul class="contacts">
      <li><svg viewBox="0 0 24 24"><path d="M6.6 10.8a15.1 15.1 0 0 0 6.6 6.6l2.2-2.2a1 1 0 0 1 1-.25 11.4 11.4 0 0 0 3.6.6 1 1 0 0 1 1 1V20a1 1 0 0 1-1 1A17 17 0 0 1 3 4a1 1 0 0 1 1-1h3.5a1 1 0 0 1 1 1c0 1.25.2 2.45.6 3.6a1 1 0 0 1-.25 1z"/></svg>555 301 4872</li>
      <li><svg viewBox="0 0 24 24"><path d="M6 2h12v6H6zM3 9h18a1 1 0 0 1 1 1v7h-4v5H6v-5H2v-7a1 1 0 0 1 1-1zm5 8v3h8v-3z"/></svg>555 301 4872</li>
      <li><svg viewBox="0 0 24 24"><path d="M2 5h20v14H2zm2 2v.5l8 5 8-5V7l-8 5z"/></svg>info@kvro.com</li>
      <li><svg viewBox="0 0 24 24"><circle cx="12" cy="12" r="10"/></svg>www.kvro.com</li>
    </ul>
    <address class="address">118 Harbor Lane<br>Suite 210, Lakeview<br>MN 55012</address>
  </div>
</section>

</body>
</html>
```